Lavoie Roofing

Want a professional looking business card

Industry/Entity Type

Business

Contact Information for Business Card

Mark Lavoie ( Owner) mark@lavoieroofing.example, www.lavoieroofing.example, Adress: 4712 Birchwood Lane Maplebrook,ON Z9Z 9Z9

```html
<!DOCTYPE html>
<html lang="en">
<head>
<meta charset="utf-8">
<title>Lavoie Roofing – Business Card</title>
<link rel="stylesheet" href="https://fonts.googleapis.com/css2?family=Montserrat:wght@800&family=Open+Sans:wght@300;400;700&display=swap">
<style>
  :root {
    --backdrop: #262626;
    --brand-blue: #2463c4;
    --brand-blue-dark: #1b4fa6;
    --brand-blue-light: #3a7ad6;
    --card-white: #ffffff;
    --card-shade: #eeeeee;
    --ink-grey: #6f6f6f;
    --ink-dark: #4a4a4a;
    --accent-blue: #4a7fd0;
  }
  * { box-sizing: border-box; margin: 0; padding: 0; }
  html, body { width: 1200px; height: 1015px; overflow: hidden; }
  body {
    background: var(--backdrop);
    font-family: "Open Sans", Arial, sans-serif;
    position: relative;
  }
  .card {
    position: absolute;
    left: 250px;
    width: 700px;
    height: 400px;
    border-radius: 26px;
    overflow: hidden;
  }
  .card--front {
    top: 80px;
    background: linear-gradient(135deg, var(--brand-blue-dark) 0%, var(--brand-blue) 45%, var(--brand-blue-light) 100%);
    display: flex;
    align-items: center;
    justify-content: center;
  }
  .card--back {
    top: 535px;
    background: linear-gradient(160deg, var(--card-white) 0%, var(--card-white) 55%, var(--card-shade) 100%);
  }
  .brand-name {
    font-family: "Montserrat", Arial, sans-serif;
    font-weight: 800;
    text-transform: uppercase;
    letter-spacing: 3px;
    display: flex;
    align-items: center;
    gap: 14px;
    white-space: nowrap;
  }
  .brand-name__mark {
    display: inline-block;
    width: 30px;
    height: 30px;
  }
  .card--front .brand-name { color: var(--card-white); font-size: 46px; }
  .card--front .brand-name__mark { background: var(--card-white); }
  .card--back .brand-name {
    position: absolute;
    left: 56px;
    top: 70px;
    color: var(--brand-blue);
    font-size: 32px;
  }
  .card--back .brand-name__mark { background: var(--brand-blue); width: 22px; height: 22px; }
  .owner {
    position: absolute;
    left: 56px;
    bottom: 70px;
  }
  .owner__name {
    font-size: 34px;
    font-weight: 300;
    color: var(--ink-grey);
    white-space: nowrap;
  }
  .owner__name strong { font-weight: 700; color: var(--ink-dark); }
  .owner__role {
    font-size: 20px;
    color: var(--accent-blue);
    margin-top: 2px;
  }
  .contact {
    position: absolute;
    left: 360px;
    top: 170px;
    list-style: none;
    font-size: 17px;
    color: var(--ink-grey);
    line-height: 1.3;
  }
  .contact__item {
    display: flex;
    align-items: flex-start;
    gap: 12px;
    margin-bottom: 14px;
    white-space: nowrap;
  }
  .contact__item--web { font-size: 21px; }
  .contact__icon { flex: 0 0 16px; width: 16px; height: 16px; margin-top: 3px; }
</style>
</head>
<body>
  <section class="card card--front" aria-label="Card front">
    <div class="brand-name"><span class="brand-name__mark"></span>Lavoie Roofing</div>
  </section>

  <section class="card card--back" aria-label="Card back">
    <div class="brand-name"><span class="brand-name__mark"></span>Lavoie Roofing</div>

    <div class="owner">
      <p class="owner__name">Mark <strong>Lavoie</strong></p>
      <p class="owner__role">Owner</p>
    </div>

    <ul class="contact">
      <li class="contact__item">
        <svg class="contact__icon" viewBox="0 0 16 16" aria-hidden="true"><path d="M8 1a5 5 0 0 0-5 5c0 4 5 9 5 9s5-5 5-9a5 5 0 0 0-5-5zm0 7a2 2 0 1 1 0-4 2 2 0 0 1 0 4z" fill="var(--brand-blue)"/></svg>
        <span>4712 Birchwood Lane Maplebrook,<br>ON Z9Z 9Z9</span>
      </li>
      <li class="contact__item">
        <svg class="contact__icon" viewBox="0 0 16 16" aria-hidden="true"><path d="M3 2h3l1 3-2 1a8 8 0 0 0 4 4l1-2 3 1v3a1 1 0 0 1-1 1A12 12 0 0 1 2 3a1 1 0 0 1 1-1z" fill="var(--brand-blue)"/></svg>
        <span>000 000 0000</span>
      </li>
      <li class="contact__item">
        <svg class="contact__icon" viewBox="0 0 16 16" aria-hidden="true"><rect x="1" y="3" width="14" height="10" rx="1" fill="var(--brand-blue)"/><path d="M1.5 4 8 9l6.5-5" stroke="#fff" stroke-width="1.2" fill="none"/></svg>
        <span>mark@lavoieroofing.example</span>
      </li>
      <li class="contact__item contact__item--web">
        <svg class="contact__icon" viewBox="0 0 16 16" aria-hidden="true"><circle cx="8" cy="8" r="6.5" fill="none" stroke="var(--brand-blue)" stroke-width="1.3"/><ellipse cx="8" cy="8" rx="2.8" ry="6.5" fill="none" stroke="var(--brand-blue)" stroke-width="1.1"/><path d="M1.5 8h13" stroke="var(--brand-blue)" stroke-width="1.1"/></svg>
        <span>www.lavoieroofing.example</span>
      </li>
    </ul>
  </section>
</body>
</html>
```